Modern Billboard Ad for Criminal Defense Firm

10.5 x 36 We're looking for something to set us apart from the local competition. Looking for sleek and modern. We're a mid-sized firm in a small market city. We want to give the artist room to be creative on this one.
Thanks

Target Market(s)

Adult clients who have been charged with a crime/DWI

Industry/Entity Type

legal

Font styles to use
Serif
Sans Serif

Requirements
Must have
• Needs to have the firm name in large lettering. Law Offices of Marcus T Whitfield. “PLLC” does not have to be included. Phone number of (555) 384-1927 should be included but not the main focus.
Nice to have
• A call to action or something similar. “Don’t go it alone, call today.”, “ Arrested?”

```html
<!DOCTYPE html>
<html lang="en">
<head>
<meta charset="utf-8">
<title>Law Offices of Marcus T Whitfield – Billboard</title>
<link rel="stylesheet" href="https://fonts.googleapis.com/css2?family=Noto+Serif:wght@700&family=Montserrat:wght@500;700&display=swap">
<style>
  :root {
    --page-bg: #e9edf3;
    --navy-deep: #02123f;
    --navy: #0a2a6b;
    --band-glow: #1f8fdc;
    --band-edge: #06306e;
    --white: #ffffff;
    --phone-blue: #23a6ee;
    --portrait-light: #b9bcc2;
    --portrait-dark: #3c3f46;
  }
  * { margin: 0; padding: 0; box-sizing: border-box; }
  html, body {
    width: 1200px; height: 1200px; overflow: hidden;
    background: var(--page-bg);
  }
  .billboard {
    position: absolute;
    left: 0; top: 425px;
    width: 1200px; height: 350px;
    overflow: hidden;
    background:
      radial-gradient(ellipse 420px 300px at 1040px 220px, rgba(20,70,160,.45), transparent 70%),
      linear-gradient(90deg, var(--navy-deep) 0%, var(--navy) 55%, var(--navy-deep) 100%);
  }
  .portrait {
    position: absolute;
    left: 0; top: 20px;
    width: 310px; height: 330px;
    background: linear-gradient(160deg, var(--portrait-light) 0%, #7d8088 45%, var(--portrait-dark) 100%);
    border-radius: 120px 120px 0 0;
  }
  .cta-band {
    position: absolute;
    left: 300px; top: 189px;
    width: 700px; height: 56px;
    background: radial-gradient(ellipse 260px 60px at 50% 50%, var(--band-glow) 0%, var(--band-edge) 60%, transparent 100%);
  }
  .firm-name {
    position: absolute;
    left: 295px; width: 805px;
    text-align: center;
    font-family: "Noto Serif", Georgia, serif;
    font-weight: 700;
    color: var(--white);
    line-height: 1;
  }
  .firm-name__main { top: 28px; font-size: 110px; letter-spacing: 2px; }
  .firm-name__sub  { top: 138px; font-size: 42px; letter-spacing: 1.5px; left: 295px; width: 795px; }
  .cta {
    position: absolute;
    left: 300px; width: 790px; top: 202px;
    text-align: center;
    font-family: "Montserrat", Arial, sans-serif;
    font-weight: 500;
    font-size: 34px;
    color: var(--white);
    line-height: 1;
  }
  .phone {
    position: absolute;
    left: 300px; width: 740px; top: 258px;
    text-align: center;
    font-family: "Montserrat", Arial, sans-serif;
    font-weight: 700;
    font-size: 86px;
    letter-spacing: 3px;
    color: var(--phone-blue);
    line-height: 1;
  }
</style>
</head>
<body>
  <section class="billboard">
    <div class="portrait" role="img" aria-label="Black and white portrait of the attorney in a suit vest and tie, jacket over his shoulder"></div>
    <div class="cta-band"></div>
    <h1 class="firm-name firm-name__main">LAW OFFICES</h1>
    <p class="firm-name firm-name__sub">OF MARCUS T WHITFIELD</p>
    <p class="cta">ARRESTED?</p>
    <p class="phone">555-384-1927</p>
  </section>
</body>
</html>
```